Business Card Design

Very plain simple card, Plain modern font. Background. Grey fading to black. Large Bright lime green text. Saying.

TWR-ZA.COM

Small other details in white text.

Irish Horse Sales . Livery . Stud . Shows

Mark Dabrowski
TWR
Birch Lodge
Carrowmede Lane
Thistlecombe
Lincolnshire
LN4 7JX

Email. Twrzap@mailvale.co.uk
Tel. 07482 936504

Industry/Entity Type

Business

Contact Information for Business Card

As below

```html
<!DOCTYPE html>
<html lang="en">
<head>
<meta charset="utf-8">
<title>TWR-ZA.COM Business Card</title>
<link href="https://fonts.googleapis.com/css2?family=Crimson+Text:wght@400&family=Carlito&display=swap" rel="stylesheet">
<style>
  :root {
    --page: #ffffff;
    --lime: #d4df26;
    --ink: #262626;
    --band: #000000;
    --grey-top: #474747;
    --grey-mid: #2a2a2a;
    --black: #000000;
    --white: #ffffff;
    --bullet: #bdbdbd;
    --icon-green: #5fa83a;
    --icon-green-dark: #3d7a22;
  }
  * { margin: 0; padding: 0; box-sizing: border-box; }
  html, body { width: 1200px; height: 1000px; overflow: hidden; background: var(--page); }
  .canvas { position: relative; width: 1200px; height: 1000px; }

  .card { position: absolute; left: 80px; top: 157px; width: 1039px; height: 685px; }
  .card__header { position: absolute; left: 0; top: 0; width: 100%; height: 240px; background: var(--lime); }
  .card__divider { position: absolute; left: 0; top: 240px; width: 100%; height: 14px; background: var(--band); }
  .card__body {
    position: absolute; left: 0; top: 254px; width: 100%; height: 431px;
    background: linear-gradient(to bottom, var(--grey-top) 0%, var(--grey-mid) 45%, var(--black) 100%);
  }

  .brand {
    position: absolute; left: 0; width: 100%; top: 42px; text-align: center;
    padding-left: 8px;
    font-family: "Carlito", "Calibri", sans-serif;
    font-weight: 400;
    font-size: 76px; line-height: 1; color: var(--ink); letter-spacing: 1px;
  }

  .contact { position: absolute; left: 304px; font-family: "Carlito", "Calibri", sans-serif;
    font-size: 26px; color: var(--ink); display: flex; align-items: center; line-height: 1; }
  .contact--email { top: 139px; }
  .contact--phone { top: 189px; }
  .contact__icon { width: 34px; height: 34px; margin-right: 24px; }

  .services {
    position: absolute; left: 57px; top: 172px;
    font-family: "Crimson Text", "Palatino Linotype", serif;
    font-size: 35px; color: var(--white); line-height: 1; letter-spacing: 0.2px;
    white-space: nowrap;
  }

  .address { position: absolute; list-style: none;
    font-family: "Crimson Text", "Palatino Linotype", serif;
    font-size: 25px; color: var(--white); line-height: 38px; white-space: nowrap; }
  .address--left { left: 63px; top: 230px; }
  .address--right { left: 343px; top: 230px; }
  .address li { display: flex; align-items: center; }
  .address--left li svg { margin-right: 20px; }
  .address--right li svg { margin-right: 12px; }
  .bullet { width: 16px; height: 16px; flex: none; }
</style>
</head>
<body>
<div class="canvas">
  <svg width="0" height="0" style="position:absolute">
    <defs>
      <symbol id="star" viewBox="0 0 16 16">
        <g stroke="var(--bullet)" stroke-width="1.2" stroke-linecap="round">
          <line x1="8" y1="1" x2="8" y2="15"/>
          <line x1="1" y1="8" x2="15" y2="8"/>
          <line x1="3" y1="3" x2="13" y2="13"/>
          <line x1="13" y1="3" x2="3" y2="13"/>
        </g>
      </symbol>
    </defs>
  </svg>

  <div class="card">
    <div class="card__header">
      <h1 class="brand">TWR-ZA.COM</h1>

      <p class="contact contact--email">
        <svg class="contact__icon" viewBox="0 0 34 34" aria-hidden="true">
          <circle cx="17" cy="17" r="16" fill="var(--icon-green)" stroke="var(--icon-green-dark)" stroke-width="1.5"/>
          <rect x="8" y="10.5" width="18" height="13" fill="#dfeecf" stroke="#2f4a1e" stroke-width="1.3"/>
          <path d="M8 10.5 L17 18 L26 10.5 M8 23.5 L14 16.5 M26 23.5 L20 16.5" fill="none" stroke="#2f4a1e" stroke-width="1.3"/>
        </svg>
        Email: Twrzap@mailvale.co.uk
      </p>

      <p class="contact contact--phone">
        <svg class="contact__icon" viewBox="0 0 34 34" aria-hidden="true">
          <circle cx="17" cy="17" r="16" fill="var(--icon-green)" stroke="var(--icon-green-dark)" stroke-width="1.5"/>
          <path d="M11 9 L14 9 L15.5 13 L13.5 14.5 C14.8 17.5 16.5 19.2 19.5 20.5 L21 18.5 L25 20 L25 23 C25 24.5 23.5 25.5 22 25 C15.5 23.5 10.5 18.5 9 12 C8.6 10.5 9.5 9 11 9 Z" fill="#ffffff"/>
        </svg>
        Telephone:&nbsp; 07482 936504
      </p>
    </div>

    <div class="card__divider"></div>

    <div class="card__body">
      <p class="services">Irish Horse Sales, Livery,&nbsp; Stud,&nbsp; Shows</p>

      <ul class="address address--left">
        <li><svg class="bullet"><use href="#star"/></svg>Mark Dabrowski</li>
        <li><svg class="bullet"><use href="#star"/></svg>TWR</li>
        <li><svg class="bullet"><use href="#star"/></svg>Birch Lodge</li>
        <li><svg class="bullet"><use href="#star"/></svg>Carrowmede Lane</li>
      </ul>

      <ul class="address address--right">
        <li><svg class="bullet"><use href="#star"/></svg>Thistlecombe</li>
        <li><svg class="bullet"><use href="#star"/></svg>Lincolnshire</li>
        <li><svg class="bullet"><use href="#star"/></svg>LN4 7JX</li>
      </ul>
    </div>
  </div>
</div>
</body>
</html>
```